Business card for builder specialising in renovations.

Need a card for our building business. Business name is under Martin Pelloe.
Have licence number on card ( 527916K)
Contact number (0400 382 615)
Want to work on logo for some business cards and shirts - something with MP or MPB or open to ideas??
No animations, No hammers. Something sharp and eye catching.
Highlight that we are a renovation specialist. Simple on front with extra details on back with some lines to jot down things.

Target Market(s)

Renovators

Industry/Entity Type

Building

Contact Information for Business Card

2 sided with room on back to jot things down.
Extra details on back so front can be simple ..like, renovations, bathrooms, decks, extensions, new builds,

Logo Text

MP

Font styles to use
Serif

Requirements
Must have
• Eye catching design .
• Name : Martin pelloe
• Licence number
• Contact number - 0400382615
Nice to have
• Some logo design that we can carry through to other forms of advertising
• Local builder
• Quality work
Should not have
• No animations

```html
<!DOCTYPE html>
<html lang="en">
<head>
<meta charset="utf-8">
<title>Martin Pelloe – Business Card</title>
<link rel="stylesheet" href="https://fonts.googleapis.com/css2?family=Tinos:wght@400;700&display=swap">
<style>
  :root {
    --card-blue: #29a8e0;
    --ink: #111111;
    --paper: #ffffff;
    --backdrop: #2b2b2b;
    --serif: "Tinos", "Times New Roman", serif;
  }
  * { box-sizing: border-box; margin: 0; padding: 0; }
  html, body { width: 1200px; height: 900px; overflow: hidden; }
  body {
    background: var(--backdrop);
    font-family: var(--serif);
    position: relative;
  }
  .card {
    position: absolute;
    width: 700px;
    height: 400px;
    overflow: hidden;
  }

  /* Front */
  .card--front { left: 170px; top: 40px; background: var(--card-blue); }
  .front__brand {
    position: absolute;
    left: 400px; top: 56px;
    width: 240px;
    text-align: center;
  }
  .brand__square {
    width: 200px; height: 200px;
    margin: 0 auto;
    background: var(--paper);
    border: 2px solid var(--ink);
  }
  .brand__name {
    font-size: 26px;
    font-weight: 700;
    color: var(--ink);
    letter-spacing: 0.5px;
    margin-top: 6px;
    white-space: nowrap;
  }
  .front__web {
    font-size: 17px;
    color: var(--paper);
    margin-top: 2px;
  }
  .services {
    position: absolute;
    left: 70px; top: 258px;
    list-style: none;
  }
  .services li {
    display: flex;
    align-items: center;
    gap: 12px;
    color: var(--paper);
    font-size: 16px;
    letter-spacing: 0.6px;
    line-height: 26px;
  }
  .services li::before {
    content: "";
    width: 11px; height: 11px;
    background: var(--ink);
    flex: none;
  }

  /* Back */
  .card--back { left: 330px; top: 460px; background: var(--paper); }
  .back__brand {
    position: absolute;
    left: 48px; top: 44px;
    width: 230px;
    text-align: center;
  }
  .back__brand .brand__square {
    width: 190px; height: 190px;
    background: var(--card-blue);
  }
  .rule {
    position: absolute;
    height: 2px;
    background: var(--card-blue);
  }
  .rule--header { left: 300px; right: 0; top: 150px; }
  .rule--base { left: 0; right: 0; top: 300px; }
  .contact {
    position: absolute;
    left: 440px; top: 96px;
    color: var(--ink);
  }
  .contact__name {
    font-size: 26px;
    color: var(--card-blue);
    letter-spacing: 0.5px;
    line-height: 50px;
  }
  .contact__role { font-size: 15px; margin-top: 6px; }
  .contact__licence { font-size: 16px; margin-top: 2px; }
  .contact__licence span { color: var(--card-blue); }
  .contact__list { list-style: none; margin-top: 4px; }
  .contact__list li {
    display: flex;
    align-items: center;
    gap: 10px;
    font-size: 16px;
    line-height: 22px;
  }
  .contact__list svg { width: 12px; height: 12px; flex: none; }
  .contact__list .accent { color: var(--card-blue); }
</style>
</head>
<body>

<section class="card card--front">
  <div class="front__brand">
    <div class="brand__square"></div>
    <p class="brand__name">MARTIN PELLOE</p>
    <p class="front__web">www.pelloebuilds.com</p>
  </div>
  <ul class="services">
    <li>RENOVATIONS</li>
    <li>BATHROOMS DECKS</li>
    <li>EXTENSIONS</li>
    <li>NEW BUILDS</li>
  </ul>
</section>

<section class="card card--back">
  <div class="back__brand">
    <div class="brand__square"></div>
    <p class="brand__name">MARTIN PELLOE</p>
  </div>
  <div class="rule rule--header"></div>
  <div class="rule rule--base"></div>
  <div class="contact">
    <p class="contact__name">MARTIN PELLOE</p>
    <p class="contact__role">Director</p>
    <p class="contact__licence"><span>Licence:</span> (527916K)</p>
    <ul class="contact__list">
      <li>
        <svg viewBox="0 0 12 12" aria-hidden="true"><path d="M2.5 1l2 2.2-1 1.3c.7 1.5 1.8 2.6 3.3 3.3l1.3-1L10.3 9 9 11C4.8 10.6 1.4 7.2 1 3z" fill="#29a8e0"/></svg>
        0400382615
      </li>
      <li>
        <svg viewBox="0 0 12 12" aria-hidden="true"><rect x="1" y="2.5" width="10" height="7" fill="none" stroke="#29a8e0" stroke-width="1.2"/><path d="M1 2.5l5 4 5-4" fill="none" stroke="#29a8e0" stroke-width="1.2"/></svg>
        info@pelloebuilds.com
      </li>
      <li>
        <svg viewBox="0 0 12 12" aria-hidden="true"><circle cx="6" cy="6" r="5" fill="#29a8e0"/><path d="M1 6h10M6 1c-2 2.5-2 7.5 0 10M6 1c2 2.5 2 7.5 0 10" fill="none" stroke="#fff" stroke-width=".8"/></svg>
        <span>www.<span class="accent">pelloebuilds</span>.com</span>
      </li>
    </ul>
  </div>
</section>

</body>
</html>
```